Amber Hill House Brochure Design

We need a brochure designed for our Aged Care Facility. We need designs that portray warmth and welcoming and at the same time something professional. We have attached the previous brochure and are looking for a modern professional brochure. We are not set on sizing and welcome ideas.

Attachments:
- There are three files attached in this brief.
- One more high res photo is available via this link: https://www.filecrate.example/s/qm42tx7wpe0kdn3/House_High-Res_18.jpg?dl=0
- Another high res file has been added and is available through this link:
https://www.filecrate.example/s/vr83nc1yuf6jlo9/House_High-Res_24.jpg?dl=0

Target Market(s)

Aged Care and families

Requirements
Must have
• Logo and contact details

```html
<!DOCTYPE html>
<html lang="en">
<head>
<meta charset="utf-8">
<title>Amber Hill House – Trifold Brochure</title>
<link rel="stylesheet" href="https://fonts.googleapis.com/css2?family=Dancing+Script:wght@500&family=Open+Sans:wght@400;600;700&family=Petit+Formal+Script&family=Roboto+Condensed:wght@400;700&display=swap">
<style>
  :root {
    --backdrop: #e6e7e8;
    --paper: #ffffff;
    --slate: #3d5b6e;
    --slate-soft: #c8d1d8;
    --ink: #1f2f3a;
    --fold: #eceff1;
  }
  html, body {
    margin: 0;
    width: 1200px;
    height: 1200px;
    overflow: hidden;
    background: var(--backdrop);
  }
  .brochure {
    position: absolute;
    left: 45px;
    top: 220px;
    width: 1110px;
    height: 760px;
    box-shadow: 0 10px 30px rgba(0,0,0,.18);
    background: var(--paper);
  }
  .brochure svg { display: block; }
  .script-copy { font-family: "Dancing Script", cursive; font-size: 23px; fill: var(--slate); }
  .brand-name { font-family: "Roboto Condensed", sans-serif; font-weight: 400; fill: var(--slate); letter-spacing: 1.5px; }
  .brand-tagline { font-family: "Open Sans", sans-serif; font-size: 9px; fill: #8a7560; letter-spacing: .3px; }
  .contact-title { font-family: "Open Sans", sans-serif; font-weight: 700; font-size: 19px; fill: var(--slate); }
  .contact-sub { font-family: "Open Sans", sans-serif; font-size: 12px; fill: var(--slate); }
  .contact-line { font-family: "Open Sans", sans-serif; font-weight: 600; font-size: 13px; fill: var(--ink); }
  .web-address { font-family: "Open Sans", sans-serif; font-weight: 600; font-size: 13px; fill: var(--paper); }
  .headline-light { font-family: "Roboto Condensed", sans-serif; font-size: 24px; fill: var(--ink); }
  .headline-bold { font-family: "Roboto Condensed", sans-serif; font-weight: 700; font-size: 36px; fill: var(--slate); }
  .promise { font-family: "Petit Formal Script", cursive; fill: var(--ink); }
  .promise-accent { fill: var(--slate); }
</style>
</head>
<body>
<div class="brochure">
<svg width="1110" height="760" viewBox="0 0 1110 760">
  <defs>
    <linearGradient id="sunlitGroup" x1="0" y1="0" x2="1" y2="1">
      <stop offset="0" stop-color="#e9dca6"/>
      <stop offset=".5" stop-color="#c9ad72"/>
      <stop offset="1" stop-color="#7d7a52"/>
    </linearGradient>
    <linearGradient id="gardenPath" x1="0" y1="0" x2="0" y2="1">
      <stop offset="0" stop-color="#3f7fc9"/>
      <stop offset=".45" stop-color="#8fb2c9"/>
      <stop offset=".7" stop-color="#b9b4a6"/>
      <stop offset="1" stop-color="#5f8a3f"/>
    </linearGradient>
    <linearGradient id="carerMoment" x1="0" y1="0" x2="1" y2="0">
      <stop offset="0" stop-color="#6e6e6e"/>
      <stop offset="1" stop-color="#c4c4c4"/>
    </linearGradient>
    <radialGradient id="loungeInterior" cx=".5" cy=".4" r=".6">
      <stop offset="0" stop-color="#eef1f0"/>
      <stop offset=".7" stop-color="#c9d0d1"/>
      <stop offset="1" stop-color="#6f9a52"/>
    </radialGradient>
    <clipPath id="loungeCircle"><circle cx="560" cy="560" r="112"/></clipPath>
    <clipPath id="middlePanel"><rect x="370" y="0" width="370" height="760"/></clipPath>
  </defs>

  <!-- panel folds -->
  <rect x="368" y="0" width="4" height="760" fill="var(--fold)"/>
  <rect x="738" y="0" width="4" height="760" fill="var(--fold)"/>

  <!-- top photo spanning left and middle panels -->
  <path role="img" aria-label="Photo of smiling elderly residents walking together outdoors in a sunlit garden"
        d="M0,0 H605 C520,115 300,250 0,285 Z" fill="url(#sunlitGroup)"/>
  <path d="M0,302 C300,268 535,125 625,0" fill="none" stroke="var(--slate)" stroke-width="14"/>

  <!-- middle panel swoosh, meeting the right panel bands at the fold -->
  <g clip-path="url(#middlePanel)">
    <path d="M655,0 C700,70 705,228 742,228" fill="none" stroke="var(--slate-soft)" stroke-width="22"/>
    <path d="M632,0 C685,60 690,196 742,196" fill="none" stroke="var(--slate)" stroke-width="12"/>
  </g>

  <!-- left panel copy -->
  <text class="script-copy" text-anchor="middle">
    <tspan x="188" y="342">Amber Hill House</tspan>
    <tspan x="188" y="372">is accredited</tspan>
    <tspan x="188" y="402">government funded place.</tspan>
  </text>
  <line x1="70" y1="425" x2="300" y2="420" stroke="var(--slate)" stroke-width="1.5"/>
  <text class="script-copy" text-anchor="middle">
    <tspan x="188" y="462">Aged care Facility</tspan>
    <tspan x="188" y="492">Offering quality</tspan>
    <tspan x="188" y="522">dignity and individuality</tspan>
    <tspan x="188" y="552">for residents and their</tspan>
    <tspan x="188" y="582">loved ones.</tspan>
  </text>

  <!-- left panel bottom photo -->
  <path role="img" aria-label="Black and white photo of a young carer chatting warmly with an elderly resident"
        d="M0,600 C120,585 260,590 370,610 V760 H0 Z" fill="url(#carerMoment)"/>

  <!-- middle panel diagonal band -->
  <path d="M405,760 C470,700 520,665 560,645 C640,600 690,560 742,545" fill="none" stroke="var(--slate)" stroke-width="14"/>

  <!-- middle panel brand -->
  <circle cx="488" cy="205" r="8" fill="var(--slate)"/>
  <text class="brand-name" x="502" y="211" font-size="17">AMBER HILL HOUSE</text>
  <text class="brand-tagline" x="555" y="228" text-anchor="middle">Quality, Dignity, Individuality</text>

  <!-- contact -->
  <text class="contact-title" x="555" y="275" text-anchor="middle">Contact us today</text>
  <text class="contact-sub" x="555" y="292" text-anchor="middle">For more information</text>
  <path d="M487,311 c2,-2 4,-2 5,0 l2,3 c1,1 0,3 -1,3 c1,3 3,5 6,6 c0,-1 2,-2 3,-1 l3,2 c2,1 2,3 0,5 c-8,3 -20,-9 -18,-18 z" fill="var(--ink)"/>
  <text class="contact-line" x="512" y="322">07 3555 0142</text>
  <path d="M492,340 a5,5 0 1 1 10,0 c0,4 -5,9 -5,9 s-5,-5 -5,-9 z" fill="var(--ink)"/>
  <circle cx="497" cy="340" r="1.8" fill="var(--paper)"/>
  <text class="contact-line">
    <tspan x="512" y="348">48 Marlow Crescent</tspan>
    <tspan x="512" y="365">(off Amber Hill Rd)</tspan>
    <tspan x="512" y="382">Wattle Vale QLD 4090</tspan>
  </text>
  <rect x="420" y="398" width="272" height="30" rx="15" fill="var(--slate)"/>
  <circle cx="440" cy="413" r="4" fill="none" stroke="var(--paper)" stroke-width="1.5"/>
  <text class="web-address" x="452" y="418">www.amberhillhouse.com.au</text>

  <!-- circular interior photo -->
  <circle cx="560" cy="560" r="118" fill="var(--slate)"/>
  <rect role="img" aria-label="Photo of a bright resident lounge opening onto a courtyard" clip-path="url(#loungeCircle)"
        x="448" y="448" width="224" height="224" fill="url(#loungeInterior)"/>

  <!-- right panel brand and headline -->
  <circle cx="842" cy="38" r="9" fill="var(--slate)"/>
  <text class="brand-name" x="858" y="45" font-size="20">AMBER HILL HOUSE</text>
  <text class="brand-tagline" x="925" y="64" text-anchor="middle">Quality, Dignity, Individuality</text>
  <text class="headline-light" x="925" y="112" text-anchor="middle">PROVIDING AGED CARE</text>
  <text class="headline-bold" x="925" y="150" text-anchor="middle">WITH QUALITY</text>

  <!-- right panel bands and garden photo -->
  <path d="M742,196 C860,196 1000,190 1110,165" fill="none" stroke="var(--slate)" stroke-width="12"/>
  <path d="M742,228 C860,228 1000,220 1110,195" fill="none" stroke="var(--slate-soft)" stroke-width="22"/>
  <path role="img" aria-label="Photo of the facility's landscaped garden courtyard with a paved path and pergola"
        d="M742,240 C860,240 1000,232 1110,207 V470 C1000,510 870,540 742,545 Z" fill="url(#gardenPath)"/>
  <path d="M742,560 C870,556 1000,525 1110,485" fill="none" stroke="var(--slate-soft)" stroke-width="20"/>
  <path d="M742,585 C870,580 1000,548 1110,505" fill="none" stroke="var(--slate)" stroke-width="12"/>

  <!-- right panel promise -->
  <text class="promise" x="925" y="650" text-anchor="middle" font-size="18">At Amber Hill House we’re</text>
  <text class="promise" x="925" y="688" text-anchor="middle" font-size="24">commited to your</text>
  <text class="promise promise-accent" x="925" y="728" text-anchor="middle" font-size="26">care and comfort</text>
</svg>
</div>
</body>
</html>
```